Current website re-design to a updated look and feel.

We currently have a website www.brightlanefreight.com that we want to give an updated look and feel to. We are a logistics company that competes with Falcora, Dw Hartley, Vanta but on a smaller scale. We want something fresh and updated. We have two locations one in downtown Chicago, IL and one in Palatine IL. We are a fun group that also gets the job done. We know we need pictures of both locations and possibly a video, but we need fresh design ideas. The 'who we are' page is really the only page that we currently want to keep. The 'what we do' page needs to be completely re-done from a look and feel for sure.

Target Market(s)

Anyone who uses Truck transportation to move their product. Mainly US manufacturers.

Industry/Entity Type

Logistics

Number of Pages Required

5+ page

Font styles to use
Sans Serif

Colors
5c91c4
0355a3
d0dfed

Requirements
Must have
• The new design must entice people to want to do business with us. The design must have locations for pictures and at least one video which we know we will have to provide. Design must be easy to navigate.

```html
<!DOCTYPE html>
<html lang="en">
<head>
<meta charset="utf-8">
<title>Brightlane Freight</title>
<link href="https://fonts.googleapis.com/css2?family=Source+Sans+3:wght@400;600;700&display=swap" rel="stylesheet">
<style>
:root{
  --blue:#0355a3;
  --blue-mid:#5c91c4;
  --blue-pale:#d0dfed;
  --ink:#333;
  --grey-bg:#f2f2f2;
  --footer:#232323;
  --white:#fff;
}
*{box-sizing:border-box;margin:0;padding:0}
html,body{width:1200px;height:3922px;overflow:hidden}
body{font-family:"Source Sans 3",Arial,sans-serif;color:var(--ink);background:var(--white);position:relative}
section,header,footer{position:absolute;left:0;width:1200px}
.btn{display:inline-block;border:2px solid currentColor;border-radius:5px;padding:8px 18px;font-size:16px;font-weight:600;text-decoration:none}
.btn-light{color:var(--white)}
.btn-dark{color:var(--blue);background:var(--white)}
.section-title{font-size:46px;font-weight:700;color:var(--blue);text-align:center}

/* header */
.site-header{top:0;height:81px;background:var(--blue)}
.brand{position:absolute;left:0;top:0;width:305px;height:81px;background:var(--white);display:flex;align-items:center;padding-left:36px;gap:12px}
.brand-dot{width:18px;height:18px;background:var(--blue);border-radius:50%}
.brand-name{font-size:30px;font-weight:600;color:var(--blue)}
.main-nav{position:absolute;left:324px;top:0;height:81px;display:flex;align-items:center;gap:24px}
.main-nav a{color:var(--white);font-size:15px;font-weight:600;text-decoration:none;display:flex;align-items:center;gap:5px}
.login{position:absolute;right:38px;top:20px;padding:7px 16px}

/* hero */
.hero{top:81px;height:599px;background:linear-gradient(180deg,#3b4a5e 0%,#a8754f 38%,#5d5f66 58%,#2c3440 100%)}
.hero-text{position:absolute;top:360px;width:100%;text-align:center;color:var(--white)}
.hero-text h1{font-size:66px;font-weight:700;line-height:1}
.hero-text p{font-size:29px;line-height:1.4;margin-top:20px}

/* quote band */
.quote-band{top:680px;height:170px;background:var(--blue);color:var(--white)}
.quote-band h2{position:absolute;left:204px;top:42px;font-size:44px;font-weight:700}
.quote-band p{position:absolute;left:204px;top:100px;font-size:24px;font-weight:700;text-transform:uppercase}
.quote-band .btn{position:absolute;left:834px;top:64px}

/* what we do */
.services{top:850px;height:980px;background:var(--grey-bg)}
.services .section-title{position:absolute;top:46px;width:100%}
.cards{position:absolute;top:141px;left:39px;display:flex;gap:18px}
.card{width:361px;height:499px;background:var(--white);position:relative}
.card-photo{height:238px}
.card h3{font-size:20px;font-weight:700;color:#222;margin:18px 24px 10px;text-transform:uppercase}
.card p{font-size:15.5px;line-height:1.55;color:#444;margin:0 24px}
.card .btn{position:absolute;right:16px;font-size:15px;padding:7px 14px}
.carriers{position:absolute;top:679px;left:39px;width:1119px;height:243px;background:var(--blue);display:flex}
.carriers-photo{width:361px;height:243px}
.carriers-copy{flex:1;text-align:center;color:var(--white);padding-top:38px}
.carriers-copy h3{font-size:20px;font-weight:700}
.carriers-copy p{font-size:15.5px;line-height:1.55;margin-top:12px}
.carriers-copy .btn{margin-top:14px;font-size:15px;padding:7px 14px}

/* vision */
.vision{top:1830px;height:588px;background:#f7f7f7}
.vision .section-title{position:absolute;top:44px;width:100%}
.video{position:absolute;left:39px;top:157px;width:528px;height:353px;background:linear-gradient(180deg,#4b5a70 0%,#b78a65 40%,#5a5d66 65%,#2d333d 100%);box-shadow:0 3px 8px rgba(0,0,0,.35)}
.video-bar{position:absolute;left:0;bottom:0;width:100%;height:30px;background:#e4e4e4;display:flex;align-items:center;gap:10px;padding:0 10px;font-size:12px;color:#333}
.video-track{flex:1;height:4px;background:#999;position:relative}
.video-track::before{content:"";position:absolute;left:0;top:0;width:40%;height:4px;background:var(--blue)}
.vision-copy{position:absolute;left:630px;top:232px;width:520px;font-size:16px;line-height:1.65;color:#333}

/* awards */
.awards{top:2418px;height:222px;background:var(--white);border-top:1px solid #e3e3e3}
.awards h2{position:absolute;top:54px;width:100%;text-align:center;color:var(--blue);font-size:25px;font-weight:700}
.badge{position:absolute;top:112px;height:58px;background:var(--blue-pale)}

/* updates */
.updates{top:2640px;height:379px;background:var(--blue);color:var(--white);text-align:center}
.updates h2{position:absolute;top:46px;width:100%;font-size:46px;font-weight:700}
.updates p{position:absolute;top:114px;width:100%;font-size:16px}
.signup-fields{position:absolute;top:195px;left:39px;display:flex;gap:21px}
.signup-fields span{width:264px;height:40px;background:var(--white);border-radius:3px;color:#999;font-size:14px;text-align:left;padding:10px 12px}
.updates .btn{position:absolute;left:549px;top:285px;font-size:15px;padding:7px 18px}

/* locations */
.locations{top:3019px;height:620px;background:#f7f7f7}
.locations .section-title{position:absolute;top:44px;width:100%}
.location{position:absolute;top:131px;width:361px}
.location-photo{height:240px}
.location-head{display:flex;align-items:center;gap:16px;margin-top:16px}
.location-head h3{font-size:21px;font-weight:600;color:var(--blue)}
.map-pill{background:var(--blue-pale);color:var(--blue);font-size:14px;border-radius:14px;padding:4px 14px;display:flex;align-items:center;gap:5px}
.location ul{list-style:none;margin-top:18px}
.location li{display:flex;gap:16px;font-size:15px;line-height:1.5;color:#444;margin-bottom:14px}
.location li svg{flex:none;margin-top:3px}

/* footer */
.site-footer{top:3639px;height:283px;background:var(--footer);color:#ddd;font-size:15px;line-height:1.6}
.site-footer h4{position:absolute;left:136px;top:54px;color:var(--white);font-size:18px;font-weight:700}
.f-col{position:absolute;top:95px}
.f-col strong{color:var(--white);display:flex;align-items:center;gap:8px;font-size:16px}
.links{position:absolute;left:896px;top:54px}
.links h4{position:static;margin-bottom:12px}
.links li{list-style:none;display:flex;align-items:center;gap:10px;line-height:1.55}
</style>
</head>
<body>

<header class="site-header">
  <div class="brand"><span class="brand-dot"></span><span class="brand-name">Brightlane Freight</span></div>
  <nav class="main-nav">
    <a href="#">WHAT WE DO</a><a href="#">HOW WE DO IT</a><a href="#">WHO WE ARE</a><a href="#">TRACKING</a>
    <a href="#"><svg width="15" height="13" viewBox="0 0 15 13"><path d="M1 1h13v8H6l-3 3V9H1z" fill="none" stroke="#fff" stroke-width="1.5"/></svg>CHAT</a>
    <a href="#">CONTACT</a>
  </nav>
  <a class="btn btn-light login" href="#">Login</a>
</header>

<section class="hero" role="img" aria-label="Highway at sunset leading toward modern office towers">
  <div class="hero-text">
    <h1>Relax. We Got This.</h1>
    <p>Cost effective solutions for warehousing and<br>distribution of your products in every situation.</p>
  </div>
</section>

<section class="quote-band">
  <h2>You Are Shipping With Care</h2>
  <p>Request a quote now to begin your delivery!</p>
  <a class="btn btn-light" href="#">REQUEST A QUOTE</a>
</section>

<section class="services">
  <h2 class="section-title">What We Do</h2>
  <div class="cards">
    <article class="card">
      <div class="card-photo" role="img" aria-label="Container port with cranes and stacked shipping containers" style="background:linear-gradient(180deg,#c9d3dc,#7d6f68 60%,#4e5560)"></div>
      <h3>Freight Management</h3>
      <p>We strive for a perfect delivery and promise to be there for anything you may need, every step of the way.</p>
      <a class="btn btn-dark" href="#" style="top:382px">Learn More</a>
    </article>
    <article class="card">
      <div class="card-photo" role="img" aria-label="Red semi truck with white trailer on the road" style="background:linear-gradient(180deg,#bcd3ea,#e2e6ea 45%,#b33a34 70%,#5b6068)"></div>
      <h3>Transportation</h3>
      <p>With a combined 500+ years of industry experience between all employees, we are the logistics company you need to get the job done right</p>
      <a class="btn btn-dark" href="#" style="top:409px">Learn More</a>
    </article>
    <article class="card">
      <div class="card-photo" role="img" aria-label="Warehouse shelving stacked with cardboard boxes" style="background:linear-gradient(180deg,#8a5a2e,#d7a867 50%,#6e4a2a)"></div>
      <h3>Warehouse &amp; Distribution</h3>
      <p>Our secure facility can accommodate large or small quantities of product. Our inventory management system provides real-time visibility.</p>
      <a class="btn btn-dark" href="#" style="top:431px">Learn More</a>
    </article>
  </div>
  <div class="carriers">
    <div class="carriers-photo" role="img" aria-label="Truck driver standing in front of a row of white trucks" style="background:linear-gradient(180deg,#dfe5ea,#8e98a3 55%,#4a5563)"></div>
    <div class="carriers-copy">
      <h3>CARRIERS</h3>
      <p><strong>Are you a carrier looking to work with Brightlane Freight?</strong><br>Find out why we have the best carrier relationships in the business.</p>
      <a class="btn btn-light" href="#">Learn More</a>
    </div>
  </div>
</section>

<section class="vision">
  <h2 class="section-title">Brightlane Freight Vision And Mission</h2>
  <div class="video" role="img" aria-label="Company video: highway at sunset beside office buildings">
    <div class="video-bar">
      <svg width="10" height="12" viewBox="0 0 10 12"><path d="M0 0l10 6-10 6z" fill="#333"/></svg>
      <span>02:00/05:03</span><span class="video-track"></span>
      <svg width="14" height="12" viewBox="0 0 14 12"><path d="M0 4h3l4-4v12L3 8H0z" fill="#333"/></svg>
      <svg width="12" height="12" viewBox="0 0 12 12"><path d="M1 11L11 1M7 1h4v4M1 7v4h4" stroke="#333" fill="none" stroke-width="1.5"/></svg>
    </div>
  </div>
  <p class="vision-copy">Lorem ipsum dolor sit amet, consectetur adipiscing elit. Vivamus tincidunt sapien et elit gravida tempus. Nulla blandit dolor scelerisque, elementum neque at, tincidunt nunc. Nullam volutpat auctor quam vitae tempus. Fusce tempus efficitur feugiat. Morbi iaculis ipsum ac nisi pharetra viverra vel a mi. Vivamus porta at urna a eleifend.</p>
</section>

<section class="awards">
  <h2>Awards</h2>
  <div class="badge" style="left:455px;width:110px"></div>
  <div class="badge" style="left:627px;width:120px;border-radius:8px"></div>
</section>

<section class="updates">
  <h2>Get Updates</h2>
  <p>We occasionally send out news and related industry articles. Sign up and we promise to deliver quality information to you.</p>
  <div class="signup-fields"><span>First Name</span><span>Last Name</span><span>Organisation</span><span>Email</span></div>
  <a class="btn btn-light" href="#">Sign Up</a>
</section>

<section class="locations">
  <h2 class="section-title">Our Locations</h2>
  <div class="location" style="left:209px">
    <div class="location-photo" role="img" aria-label="Two-storey brick office building in Palatine" style="background:linear-gradient(180deg,#a9c6e6,#9d7a60 55%,#6d7a5e)"></div>
    <div class="location-head"><h3>Palatine</h3><span class="map-pill"><svg width="10" height="14" viewBox="0 0 10 14"><path d="M5 0a5 5 0 0 1 5 5c0 4-5 9-5 9S0 9 0 5a5 5 0 0 1 5-5z" fill="#0355a3"/><circle cx="5" cy="5" r="2" fill="#d0dfed"/></svg>View map</span></div>
    <ul>
      <li><svg width="12" height="16" viewBox="0 0 10 14"><path d="M5 0a5 5 0 0 1 5 5c0 4-5 9-5 9S0 9 0 5a5 5 0 0 1 5-5z" fill="#0355a3"/><circle cx="5" cy="5" r="2" fill="#fff"/></svg><span>418 W Orchard Ave Suite 210<br>Palatine, IL 60067</span></li>
      <li><svg width="14" height="14" viewBox="0 0 14 14"><path d="M3 0l3 3-2 2c1 2 3 4 5 5l2-2 3 3-2 3C6 14 0 8 0 3z" fill="#0355a3"/></svg><span>Phone: 555.014.2200</span></li>
      <li><svg width="14" height="11" viewBox="0 0 14 11"><rect width="14" height="11" fill="#0355a3"/><path d="M0 0l7 6 7-6" stroke="#fff" fill="none"/></svg><span>Information: info@brightlanefreight.com</span></li>
    </ul>
  </div>
  <div class="location" style="left:630px">
    <div class="location-photo" role="img" aria-label="Modern glass and white office building in Chicago" style="background:linear-gradient(180deg,#b8d2ee,#e6eaee 50%,#8d99a6)"></div>
    <div class="location-head"><h3>Chicago</h3><span class="map-pill"><svg width="10" height="14" viewBox="0 0 10 14"><path d="M5 0a5 5 0 0 1 5 5c0 4-5 9-5 9S0 9 0 5a5 5 0 0 1 5-5z" fill="#0355a3"/><circle cx="5" cy="5" r="2" fill="#d0dfed"/></svg>View map</span></div>
    <ul>
      <li><svg width="12" height="16" viewBox="0 0 10 14"><path d="M5 0a5 5 0 0 1 5 5c0 4-5 9-5 9S0 9 0 5a5 5 0 0 1 5-5z" fill="#0355a3"/><circle cx="5" cy="5" r="2" fill="#fff"/></svg><span>75 Harbor Row Suite 40<br>Chicago, IL 60505</span></li>
      <li><svg width="14" height="14" viewBox="0 0 14 14"><path d="M3 0l3 3-2 2c1 2 3 4 5 5l2-2 3 3-2 3C6 14 0 8 0 3z" fill="#0355a3"/></svg><span>Phone: 555.019.4400</span></li>
      <li><svg width="14" height="11" viewBox="0 0 14 11"><rect width="14" height="11" fill="#0355a3"/><path d="M0 0l7 6 7-6" stroke="#fff" fill="none"/></svg><span>Information: info@brightlanefreight.com</span></li>
    </ul>
  </div>
</section>

<footer class="site-footer">
  <h4>CONTACT</h4>
  <div class="f-col" style="left:136px">
    <strong><svg width="13" height="13" viewBox="0 0 14 14"><path d="M3 0l3 3-2 2c1 2 3 4 5 5l2-2 3 3-2 3C6 14 0 8 0 3z" fill="#5c91c4"/></svg>Phone</strong>
    Office: 555.014.2200<br>Warehouse: 555.014.2202
    <strong><svg width="14" height="13" viewBox="0 0 14 13"><rect x="3" y="0" width="8" height="4" fill="#5c91c4"/><rect x="0" y="4" width="14" height="6" fill="#5c91c4"/><rect x="3" y="8" width="8" height="5" fill="#fff"/></svg>Fax</strong>
    555.014.2201
  </div>
  <div class="f-col" style="left:420px">
    <strong><svg width="14" height="11" viewBox="0 0 14 11"><rect width="14" height="11" fill="#5c91c4"/><path d="M0 0l7 6 7-6" stroke="#232323" fill="none"/></svg>Email</strong>
    Rates: rates@brightlanefreight.com<br>Warehouse: warehouse@brightlanefreight.com<br>Information: info@brightlanefreight.com
  </div>
  <div class="links">
    <h4>USERFUL LINKS</h4>
    <ul>
      <li><svg width="7" height="10" viewBox="0 0 7 10"><path d="M1 1l4 4-4 4" stroke="#ddd" fill="none" stroke-width="1.5"/></svg>WHAT WE DO</li>
      <li><svg width="7" height="10" viewBox="0 0 7 10"><path d="M1 1l4 4-4 4" stroke="#ddd" fill="none" stroke-width="1.5"/></svg>HOW WE DO IT</li>
      <li><svg width="7" height="10" viewBox="0 0 7 10"><path d="M1 1l4 4-4 4" stroke="#ddd" fill="none" stroke-width="1.5"/></svg>WHO WE ARE</li>
      <li><svg width="7" height="10" viewBox="0 0 7 10"><path d="M1 1l4 4-4 4" stroke="#ddd" fill="none" stroke-width="1.5"/></svg>TRACKING</li>
    </ul>
  </div>
</footer>

</body>
</html>
```